Web Design Project

I work in a sign company that print banners, back light films, and vinyl lettering. We also create metal store signs that lights up. We have a laser cutter that can cut plastics and a waterjet that can cut stainless steel.
Job: Create a homepage
Requirements:
1. Keep it simple and neat, I do not want it to be messy. (Similar to this website, quince, or this http://www.plaquevora.example/)
2. A navigation bar that has (Will help if you show a template for one of these links):
-Home
-Signs
-Banners
-Lettering
-Prints
-Gallery
3.Bottom of the page
-Abous us
-Shipping and Returning Policy
-Resellers
4.Other (Somewhere easy to find)
-Login
-Shopping Cart
-Upload
Updates
Nice job designers. I am currently working on the Site's logo, so I will be posting that up later.
I would like you guys to change the selection on the navigation bar.
It should only have:
Banners
Lettering
Prints
Gallery
Keep up the good work
Sorry for the bad update, the Navigation bar should have:
Home
Signs
Banners
Lettering
Prints
Gallery

```html
<!DOCTYPE html>
<html lang="en">
<head>
<meta charset="utf-8">
<title>Varnel – Signs, Banners &amp; Lettering</title>
<link href="https://fonts.googleapis.com/css2?family=Arimo:wght@400;700&family=Alegreya+Sans:wght@700;800&display=swap" rel="stylesheet">
<style>
:root{
  --red:#a3111b;
  --red-dark:#7d0a12;
  --ink:#222;
  --text:#333;
  --muted:#666;
  --nav-top:#5a5a5a;
  --nav-bottom:#2b2b2b;
  --panel-border:#cfcfcf;
  --band:#000;
  --light:#ececec;
  --white:#fff;
}
*{box-sizing:border-box;margin:0;padding:0}
html,body{width:834px;height:1200px;overflow:hidden}
body{position:relative;background:var(--white);font-family:"Arimo",Arial,sans-serif;color:var(--text)}
.abs{position:absolute}

/* header */
.site-header{left:0;top:0;width:834px;height:87px;background:linear-gradient(#fff,#e4e4e4)}
.brand{left:38px;top:14px;display:flex;align-items:center;gap:8px}
.brand-mark{width:12px;height:12px;background:var(--red)}
.brand-name{font-weight:700;font-size:52px;color:var(--ink);letter-spacing:1px;line-height:1}
.account-links{right:21px;top:12px;font-size:11px;font-weight:700;color:#111}
.utility-links{right:20px;top:42px;display:flex;gap:10px;font-size:11px;color:#444}
.utility-links span{display:flex;align-items:center;gap:4px}
.utility-links svg{width:20px;height:20px}

/* navigation */
.main-nav{left:16px;top:87px;width:801px;height:28px;background:linear-gradient(var(--nav-top),var(--nav-bottom));border-radius:3px 3px 0 0;display:flex}
.main-nav a{color:#fff;text-decoration:none;font-size:11px;line-height:28px;text-align:center;border-right:1px solid #1c1c1c;box-shadow:1px 0 0 #666}
.nav-upload{position:absolute;left:578px;top:0;width:93px;height:28px;background:linear-gradient(#b3121c,var(--red-dark));color:#fff;font-size:11px;display:flex;align-items:center;justify-content:center;gap:6px}
.nav-search{position:absolute;left:675px;top:5px;width:117px;height:18px;background:#fff;border-radius:4px;font-size:9px;color:#999;padding-left:18px;line-height:18px}
.nav-search svg{position:absolute;left:5px;top:4px}

/* hero */
.hero-band{left:0;top:115px;width:834px;height:268px;background:var(--band)}
.hero-panel{left:17px;top:124px;width:800px;height:250px;background:linear-gradient(90deg,#fff 55%,#f1f1f1);border-radius:10px}
.hero-image{left:33px;top:137px;width:467px;height:225px;background:linear-gradient(90deg,#5a3a22,#4a2e1b 60%,#6b4426)}
.hero-title{left:517px;top:190px;font-family:"Alegreya Sans",sans-serif;font-weight:800;font-size:29px;color:#111}
.hero-copy{left:517px;top:234px;width:286px;font-size:10.2px;line-height:15px;color:#222;text-align:justify}
.hero-dots{left:514px;top:334px;display:flex;gap:6px}
.hero-dots i{width:10px;height:10px;border-radius:50%;background:#111}
.hero-dots i:first-child{background:var(--red)}
.cta{left:624px;top:313px;width:174px;height:36px;border-radius:4px;background:linear-gradient(#b8131e,var(--red-dark));color:#fff;font-family:"Alegreya Sans",sans-serif;font-weight:800;font-size:18px;padding-left:16px;line-height:36px}
.cta span{position:absolute;right:8px;top:7px;width:22px;height:22px;border-radius:50%;background:#3a0508;color:#fff;font-size:12px;line-height:22px;text-align:center}

/* info strip */
.info-strip{left:0;top:383px;width:834px;height:77px;background:var(--light);border-bottom:1px solid #ddd}
.info-btn{top:403px;width:253px;height:38px;background:repeating-linear-gradient(135deg,#e3e3e3 0 14px,#f3f3f3 14px 28px);border:1px solid #d3d3d3;font-family:"Alegreya Sans",sans-serif;font-weight:700;font-size:14px;color:#333;text-align:center;line-height:38px}
.info-btn.is-active{background:linear-gradient(#b3121c,var(--red-dark));color:#f2d6d6;border-color:var(--red-dark)}

/* sidebar */
.side-box{left:17px;width:179px;border:1px solid var(--panel-border);border-radius:4px;background:#fff}
.side-head{height:30px;background:linear-gradient(#8a8a8a,#3d3d3d);color:#fff;font-weight:700;font-size:13px;line-height:30px;padding-left:28px;border-radius:3px 3px 0 0}
.side-select{margin:2px 0 0;height:28px;background:var(--red);padding:4px 6px;position:relative}
.side-select div{height:20px;background:#fff;font-size:10px;line-height:20px;padding-left:8px;color:#111;border:1px solid #888}
.side-select b{position:absolute;right:9px;top:5px;width:24px;height:18px;background:linear-gradient(#fff,#ccc);border-left:1px solid #aaa;font-size:9px;text-align:center;line-height:18px;color:#333}
.side-list{list-style:none;padding:6px 0 0 34px;font-size:10px;line-height:21px;color:#111}
.scroll{position:absolute;right:10px;width:4px;height:98px;background:#ddd}
.scroll i{position:absolute;left:0;top:0;width:4px;height:22px}
.partner-grid{display:grid;grid-template-columns:1fr 1fr;gap:14px 20px;padding:12px 26px}
.partner-badge{height:48px;background:#d8d8d8;border-radius:6px}
.newsletter-form{display:flex;gap:2px;padding:6px}
.newsletter-form div{flex:1;height:20px;border:1px solid #aaa;font-size:10px;color:#666;line-height:20px;padding-left:12px}
.newsletter-form b{width:24px;height:20px;border:1px solid #aaa;background:linear-gradient(#fff,#ddd);font-size:10px;font-weight:400;text-align:center;line-height:20px}

/* featured */
.featured{left:214px;top:480px;width:599px;height:632px;border:1px solid var(--panel-border);border-radius:4px}
.featured-head{height:32px;background:linear-gradient(#4d4d4d,#2a2a2a);color:#fff;font-weight:700;font-size:13px;line-height:32px;padding-left:22px;border-radius:3px 3px 0 0}
.bar{height:27px;background:linear-gradient(#a5a5a5,#838383);color:#fff;font-size:13px;line-height:27px;padding-left:22px;position:relative}
.bar::after{content:"";position:absolute;right:14px;top:8px;border:6px solid transparent;border-left:8px solid #444;border-right:0}
.featured .bar-details{position:absolute;left:0;top:274px;width:597px}
.product-card{top:75px;width:131px;height:175px;border:1px solid #ccc;border-radius:7px;background:linear-gradient(#fff,#f2f2f2);box-shadow:0 1px 2px rgba(0,0,0,.1)}
.product-thumb{position:absolute;left:10px;top:14px;width:109px;height:84px}
.product-name{position:absolute;left:0;top:112px;width:100%;text-align:center;font-weight:700;font-size:10.5px;color:#111}
.product-details{position:absolute;left:12px;top:138px;width:55px;height:18px;border-radius:3px;background:linear-gradient(#888,#555);color:#fff;font-weight:700;font-size:9.5px;text-align:center;line-height:18px}
.product-price{position:absolute;right:10px;top:136px;font-weight:700;font-size:20px;color:#444}
.details-copy{left:0;top:303px;width:597px;padding:10px 20px 0;font-size:9.9px;line-height:19.3px;color:#222;text-align:justify}
.details-copy p+p{margin-top:13px}

/* footer */
.footer-rule{left:0;top:1133px;width:834px;height:4px;background:#e6e6e6}
.footer-links{left:0;top:1144px;width:834px;text-align:center;font-size:10.5px;color:var(--red)}
.footer-links span{color:#555;margin:0 5px}
.footer-bar{left:0;top:1173px;width:834px;height:27px;background:#ececec;border-top:1px solid #ddd;text-align:center;font-size:10px;color:#666;line-height:26px}
.footer-bar b{font-weight:400;color:#111;margin-left:8px}
</style>
</head>
<body>

<header class="site-header abs"></header>
<div class="brand abs"><span class="brand-name">Varnel</span><span class="brand-mark"></span></div>
<div class="account-links abs">Login | Help Center | 1.800.555.0142</div>
<div class="utility-links abs">
  <span><svg viewBox="0 0 20 20"><rect x="4" y="2" width="12" height="16" rx="1" fill="#333"/><rect x="6" y="4" width="8" height="3" fill="#ccc"/><g fill="#ccc"><rect x="6" y="9" width="2" height="2"/><rect x="9" y="9" width="2" height="2"/><rect x="12" y="9" width="2" height="2"/><rect x="6" y="12" width="2" height="2"/><rect x="9" y="12" width="2" height="2"/><rect x="12" y="12" width="2" height="2"/></g></svg>Pricing &amp; shipping</span>
  <span><svg viewBox="0 0 20 20"><rect x="7" y="2" width="6" height="10" rx="3" fill="#333"/><path d="M5 9a5 5 0 0 0 10 0M10 14v4M7 18h6" stroke="#333" stroke-width="1.5" fill="none"/></svg>Click to Chat</span>
  <span><svg viewBox="0 0 20 20"><circle cx="7" cy="6" r="3" fill="#333"/><path d="M2 17c0-5 10-5 10 0z" fill="#333"/><rect x="11" y="4" width="7" height="9" fill="none" stroke="#333"/></svg>My Desing</span>
  <span><svg viewBox="0 0 20 20"><path d="M1 4h3l2 9h10l2-7H5" stroke="#333" stroke-width="1.6" fill="none"/><circle cx="8" cy="16" r="1.5" fill="#333"/><circle cx="15" cy="16" r="1.5" fill="#333"/></svg>Cart Items</span>
</div>

<nav class="main-nav abs">
  <a style="width:69px">Home</a><a style="width:82px">Signs</a><a style="width:82px">Banners</a><a style="width:87px">Lettering</a><a style="width:77px">Prints</a><a style="width:93px">Gallery</a><a style="width:88px;border:0;box-shadow:none">Support</a>
  <div class="nav-upload"><svg width="16" height="14" viewBox="0 0 16 14"><rect x="1" y="7" width="14" height="6" fill="#eee"/><path d="M8 1l4 4H9v4H7V5H4z" fill="#f2c200"/></svg>Upload</div>
  <div class="nav-search"><svg width="9" height="9" viewBox="0 0 9 9"><circle cx="3.5" cy="3.5" r="2.5" stroke="#888" fill="none"/><path d="M5.5 5.5l3 3" stroke="#888"/></svg>Search</div>
</nav>

<section class="hero-band abs"></section>
<div class="hero-panel abs"></div>
<div class="hero-image abs" role="img" aria-label="Living room with a brown leather sofa in front of a wall decorated with white birch tree vinyl decals"></div>
<h1 class="hero-title abs">Printing banners</h1>
<p class="hero-copy abs">It was popularised in the 1960s with the release of Letterpane sheets containing Lorem Ipsum passages, and more recently with desktop publishing software like Folio Layout including versions of Lorem Ipsum.</p>
<div class="hero-dots abs"><i></i><i></i><i></i></div>
<div class="cta abs">Get Started<span>&#10095;</span></div>

<section class="info-strip abs"></section>
<div class="info-btn abs" style="left:20px">How to Order</div>
<div class="info-btn abs is-active" style="left:289px">Why Buy Varnel</div>
<div class="info-btn abs" style="left:557px">Quick Order Status</div>

<aside class="side-box abs" style="top:480px;height:180px">
  <div class="side-head">Products</div>
  <div class="side-select"><div>Letterring</div><b>&#8964;</b></div>
  <ul class="side-list"><li>Car Lettering</li><li>Car Window Lettering</li><li>Die-Cut Decals</li><li>Etched Glass Decals</li><li>Store Window Lettering</li></ul>
  <div class="scroll" style="top:72px"><i style="background:#b5632a"></i></div>
</aside>

<aside class="side-box abs" style="top:677px;height:180px">
  <div class="side-head">Browse by Industry</div>
  <div class="side-select"><div></div><b>&#8964;</b></div>
  <ul class="side-list"><li>Real Estate</li><li>Political</li><li>Cleaning</li><li>Daycare</li><li>Finance and Insurance</li></ul>
  <div class="scroll" style="top:72px"><i style="background:#111"></i></div>
</aside>

<aside class="side-box abs" style="top:885px;height:162px">
  <div class="side-head">Partners</div>
  <div class="partner-grid"><div class="partner-badge"></div><div class="partner-badge"></div><div class="partner-badge"></div><div class="partner-badge"></div></div>
</aside>

<aside class="side-box abs" style="top:1057px;height:53px">
  <div class="side-head" style="height:22px;line-height:22px;padding-left:20px">Newsletter</div>
  <div class="newsletter-form" style="padding-top:4px"><div>Your mail ID here</div><b>Go</b></div>
</aside>

<main class="featured abs">
  <div class="featured-head">Featured Products</div>
  <div class="bar" style="margin-top:2px">Shop Window Signs</div>
  <div class="product-card abs" style="left:12px"><div class="product-thumb" role="img" aria-label="Shop window graphic showing a fashion shopper" style="background:linear-gradient(#8aa1b3,#c9c2b8)"></div><div class="product-name">Window Graphics</div><div class="product-details">Details</div><div class="product-price">$55</div></div>
  <div class="product-card abs" style="left:154px"><div class="product-thumb" role="img" aria-label="Assorted colorful printed stickers" style="background:linear-gradient(135deg,#c43a2e,#e9e3cf 45%,#2f5fa8)"></div><div class="product-name">Stickers</div><div class="product-details">Details</div><div class="product-price">$55</div></div>
  <div class="product-card abs" style="left:301px"><div class="product-thumb" role="img" aria-label="Monogram vinyl lettering on a beige wall" style="background:linear-gradient(#d8c9b1,#b9a98f)"></div><div class="product-name">Vinyl Lettering</div><div class="product-details">Details</div><div class="product-price">$55</div></div>
  <div class="product-card abs" style="left:447px"><div class="product-thumb" role="img" aria-label="Orange graphic poster" style="background:linear-gradient(90deg,#e2962a,#f2e4cf)"></div><div class="product-name">Posters</div><div class="product-details">Details</div><div class="product-price">$55</div></div>
  <div class="bar bar-details">Product Details</div>
  <div class="details-copy abs">
    <p>Design custom vinyl lettering online today at Plaquevora.com! Self adhesive vinyl lettering is a professional and convenient way to show off your business information with vivid, solid colored vinyl decals that are easy to apply and will last for years. Vinyl window lettering is available in a variety of fonts and colors and can be applied to any flat surface. This material works great for vehicle lettering, machine lettering, door lettering and, of course, inside window lettering and outside window lettering. For front adhesive window lettering, select the Inside Glass option.</p>
    <p>Unlike other sign companies, Plaquevora.com doesn't charge by the color. Your vinyl lettering signs can be any color you'd like, all for the same low price! For classic single-color adhesive lettering, choose vinyl car lettering, car window lettering or store window lettering. Choose white vinyl window letters for tinted windows and pick from any of our predesigned templates. Set a grey background in your design to make white lettering more visible on your computer. Create multi-colored sign lettering and logos with die-cut decals, or create a more modern look with etched glass lettering.</p>
    <p>Its important to remember that when it comes to vinyl lettering decals, less is more. Choose a simple, bold font that is easy to read (cursive/script fonts are not recommended). In addition, to ensure that your vinyl truck lettering, fleet registry lettering or boat lettering will be visible from a distance, we recommend designing it with each line no smaller than 1.5" tall. See Plaquevora.com's Letter Visibility Chart for more information.</p>
  </div>
</main>

<div class="footer-rule abs"></div>
<nav class="footer-links abs">home<span>|</span>banner<span>|</span>backlight film<span>|</span>vinyl<span>|</span>pcb poster<span>|</span>custom works<span>|</span>support<span>|</span>Abous us<span>|</span>Shipping and Returning Policy<span>|</span>Resellers</nav>
<footer class="footer-bar abs">Copyright © 2012 varnel. All rights reserved. <b>Terms of Use | Privacy Policy</b></footer>

</body>
</html>
```